Need a new design for Glass Cleaner label. The brand name already exists i.e. BRIXO. Pell is the company name. Looking for new design. It's application is for cleaning glasses in houses, cars, offices e.t.c. Our product gives streak free shine and anti static effect. Images of old label design is attached. Bottle will be same as before. It's better to show a car as well in the design but not necessary. New logo's of brixo can also be designed.

Target Market(s)

Household and automobile

Industry/Entity Type

It Company

```html
<!DOCTYPE html>
<html lang="en">
<head>
<meta charset="utf-8">
<title>BRIXO Glass Cleaner Label</title>
<link rel="stylesheet" href="https://fonts.googleapis.com/css2?family=Exo+2:ital,wght@1,800&family=Fjalla+One&family=Merriweather:ital,wght@1,700&display=swap">
<style>
  :root {
    --page: #ffffff;
    --sky-light: #d6f1fc;
    --sky-mid: #8fd3f2;
    --sky-deep: #3d9fd6;
    --navy: #1a4a8c;
    --red: #e3141b;
    --white: #ffffff;
    --ring: #c9ced4;
    --photo-a: #a9d2e8;
    --photo-b: #5f6a74;
  }
  html, body {
    margin: 0;
    padding: 0;
    width: 795px;
    height: 1200px;
    overflow: hidden;
    background: var(--page);
  }
  .label {
    position: absolute;
    left: 97px;
    top: 100px;
    width: 600px;
    height: 1000px;
  }
  .brand-mark {
    font-family: "Merriweather", serif;
    font-style: italic;
    font-weight: 700;
    font-size: 64px;
    fill: var(--white);
  }
  .product-type {
    font-family: "Fjalla One", sans-serif;
    font-size: 82px;
    fill: var(--white);
    stroke: var(--navy);
    stroke-width: 7px;
    paint-order: stroke;
  }
  .product-name {
    font-family: "Exo 2", sans-serif;
    font-style: italic;
    font-weight: 800;
    font-size: 152px;
    fill: var(--red);
    stroke: var(--white);
    stroke-width: 8px;
    paint-order: stroke;
  }
  .claim {
    font-family: "Merriweather", serif;
    font-style: italic;
    font-weight: 700;
    font-size: 36px;
    fill: var(--navy);
  }
</style>
</head>
<body>
<svg class="label" viewBox="0 0 600 1000" xmlns="http://www.w3.org/2000/svg">
  <defs>
    <linearGradient id="label-fill" x1="1" y1="0" x2="0" y2="1">
      <stop offset="0" stop-color="var(--sky-deep)"/>
      <stop offset="0.35" stop-color="var(--sky-mid)"/>
      <stop offset="0.7" stop-color="var(--sky-light)"/>
      <stop offset="1" stop-color="var(--sky-mid)"/>
    </linearGradient>
    <radialGradient id="label-glow" cx="0.6" cy="0.05" r="0.6">
      <stop offset="0" stop-color="#ffffff" stop-opacity="0.55"/>
      <stop offset="1" stop-color="#ffffff" stop-opacity="0"/>
    </radialGradient>
    <linearGradient id="window-photo" x1="0" y1="0" x2="1" y2="1">
      <stop offset="0" stop-color="#eef6fb"/>
      <stop offset="1" stop-color="var(--photo-a)"/>
    </linearGradient>
    <linearGradient id="car-photo" x1="0" y1="0" x2="1" y2="1">
      <stop offset="0" stop-color="#9aa3ab"/>
      <stop offset="1" stop-color="var(--photo-b)"/>
    </linearGradient>
    <clipPath id="label-shape">
      <path d="M 420 0 L 570 0 Q 600 0 600 30 L 600 975 Q 600 1000 575 1000 L 25 1000 Q 0 1000 0 975 L 0 500 Q 0 470 20 445 L 385 20 Q 400 0 420 0 Z"/>
    </clipPath>
    <path id="claim-one-path" d="M 70 640 Q 240 580 380 720"/>
    <path id="claim-two-path" d="M 300 800 Q 480 770 600 900"/>
  </defs>

  <g clip-path="url(#label-shape)">
    <rect class="label-ground" width="600" height="1000" fill="url(#label-fill)"/>
    <rect width="600" height="1000" fill="url(#label-glow)"/>

    <g class="photo-window">
      <circle cx="120" cy="780" r="138" fill="var(--ring)"/>
      <circle cx="120" cy="780" r="124" fill="url(#window-photo)" role="img" aria-label="Photo of a hand wiping a house window with a cloth"/>
    </g>
    <g class="photo-car">
      <circle cx="350" cy="960" r="196" fill="var(--ring)"/>
      <circle cx="350" cy="960" r="180" fill="url(#car-photo)" role="img" aria-label="Photo of a hand cleaning a car dashboard with a blue cloth"/>
    </g>
  </g>

  <text class="brand-mark" x="430" y="205">Pell</text>

  <text class="product-type" x="580" y="415" text-anchor="end" transform="rotate(-3 580 415)">glass cleaner</text>
  <text class="product-name" x="580" y="565" text-anchor="end">BRIXO</text>

  <text class="claim"><textPath href="#claim-one-path">streak free shine</textPath></text>
  <text class="claim"><textPath href="#claim-two-path">anti static effect</textPath></text>
</svg>
</body>
</html>
```